Web Developer Needs a Business Card Design

I need a personal business card design that represents me as a web developer for potential employers. I would like the background to be a dark color on the front for contrast with my logo and name. The back will have all my information along with a smaller version of the logo. I want something with a modern look and feel, not too conservative. This will be used for potential employers and freelance work.

Industry/Entity Type

Business

Contact Information for Business Card

Front should have my logo and name. The back should have all my personal information which would include: name: Tom Brevardi, phone: 570-614-9083, email: tombrevardi@mailwisp.com, website url: www.tombrevardi.com, logo, web developer.

Font styles to use
Sans Serif

Requirements
Must have
• Must include my logo. The color palette base color will be the logo color.

```html
<!DOCTYPE html>
<html lang="en">
<head>
<meta charset="utf-8">
<title>Tom Brevardi – Business Card</title>
<link rel="stylesheet" href="https://fonts.googleapis.com/css2?family=Ubuntu:wght@400;500&display=swap">
<style>
  :root {
    --teal: #8fd3c7;
    --teal-deep: #6fc2b4;
    --ink: #0b0b0b;
    --paper: #f7f7f5;
    --backdrop: #e4e2dd;
  }
  * { margin: 0; padding: 0; box-sizing: border-box; }
  html, body {
    width: 1200px; height: 780px; overflow: hidden;
    background: var(--backdrop);
    font-family: "Ubuntu", sans-serif;
  }
  .sheet {
    position: relative; width: 1200px; height: 780px;
    display: flex; align-items: center; justify-content: center; gap: 40px;
  }
  .card {
    position: relative; width: 540px; height: 309px;
    box-shadow: 0 10px 28px rgba(0,0,0,.22);
    overflow: hidden;
  }
  .card-art { position: absolute; inset: 0; width: 100%; height: 100%; }

  /* Information side */
  .info-identity {
    position: absolute; left: 30px; top: 96px;
    display: flex; align-items: center; gap: 14px;
    color: var(--teal-deep);
  }
  .logo-disc {
    width: 74px; height: 74px; border-radius: 50%;
    border: 6px solid var(--teal); flex: none;
  }
  .holder-name {
    font-size: 22px; font-weight: 500; letter-spacing: .3px;
    text-transform: uppercase; line-height: 1.05; white-space: nowrap;
  }
  .holder-title { font-size: 15px; font-weight: 400; margin-top: 3px; }
  .contact-list {
    position: absolute; left: 352px; top: 118px;
    list-style: none; color: var(--teal);
    font-size: 13.5px; line-height: 1.6; white-space: nowrap;
  }

  /* Logo side */
  .front-name {
    position: absolute; left: 36px; top: 138px;
    font-size: 27px; font-weight: 500; letter-spacing: .5px;
    text-transform: uppercase; color: var(--ink); white-space: nowrap;
  }
</style>
</head>
<body>
<main class="sheet">

  <section class="card card-info" aria-label="Business card, information side">
    <svg class="card-art" viewBox="0 0 540 309" aria-hidden="true">
      <rect width="540" height="309" fill="var(--paper)"/>
      <path d="M348,0 Q294,150 322,309 L540,309 L540,0 Z" fill="var(--teal)"/>
      <path d="M356,0 Q302,150 330,309 L540,309 L540,0 Z" fill="var(--ink)"/>
    </svg>
    <div class="info-identity">
      <span class="logo-disc"></span>
      <div>
        <p class="holder-name">Tom Brevardi</p>
        <p class="holder-title">Web Developer</p>
      </div>
    </div>
    <ul class="contact-list">
      <li>570-614-9083</li>
      <li>tombrevardi@mailwisp.com</li>
      <li>www.tombrevardi.com</li>
    </ul>
  </section>

  <section class="card card-front" aria-label="Business card, logo side">
    <svg class="card-art" viewBox="0 0 540 309" aria-hidden="true">
      <rect width="540" height="309" fill="var(--ink)"/>
      <path d="M0,78 Q270,128 540,78 L540,231 Q270,181 0,231 Z" fill="var(--teal)"/>
      <circle cx="360" cy="154.5" r="56" fill="var(--ink)"/>
      <circle cx="360" cy="154.5" r="44" fill="var(--teal)"/>
    </svg>
    <p class="front-name">Tom Brevardi</p>
  </section>

</main>
</body>
</html>
```